Dribblecake Bites
2 x business cards, letter head, with complements and envelopes
Dribblecake Bites - Food
Creative Brief
Bright & Fun-filled
Percy Lantern
Managing Director
NA
Percy.Lantern@dribblecakebites.com.au
www.dribblecakebites.com.au
card 2 Teodor Blum Business Manager 0417583926 Teodorblum@quillnet.com www.dribblecakebites.com.au
logo ect

```html
<!DOCTYPE html>
<html lang="en">
<head>
<meta charset="utf-8">
<title>Dribblecake Bites – Business Cards</title>
<link rel="stylesheet" href="https://fonts.googleapis.com/css2?family=Baloo+2:wght@800&family=Arimo:wght@400;700&display=swap">
<style>
  :root {
    --stage: #3b3b3b;
    --card: #f6d6bd;
    --brown: #5a2a12;
    --brown-dark: #4a210d;
    --orange: #b8560e;
    --tagline: #c0282a;
    --ink: #4a3a30;
    --white: #ffffff;
    --motif: #eec2a2;
  }
  * { margin: 0; padding: 0; box-sizing: border-box; }
  html, body { width: 1200px; height: 741px; overflow: hidden; }
  body { background: var(--stage); font-family: "Arimo", Arial, sans-serif; position: relative; }

  .card {
    position: absolute; width: 552px; height: 322px;
    background: var(--card); overflow: hidden;
  }
  .card--front-1 { left: 36px; top: 43px; }
  .card--back-1  { left: 600px; top: 43px; }
  .card--front-2 { left: 36px; top: 377px; }
  .card--back-2  { left: 600px; top: 377px; }

  .band { position: absolute; left: 0; width: 100%; }
  .band--top { top: 0; height: 26px; }
  .band--bottom { bottom: 0; height: 30px; }

  .brand { position: absolute; left: 72px; top: 34px; }
  .brand__name {
    font-family: "Baloo 2", "Arial Rounded MT Bold", sans-serif;
    font-weight: 800; font-size: 50px; line-height: 1; color: var(--brown);
    display: flex; align-items: center; gap: 10px; letter-spacing: -0.5px;
  }
  .brand__dot { width: 18px; height: 18px; border-radius: 50%; background: var(--orange); }
  .brand__tagline {
    margin-top: 2px; font-weight: 700; font-style: italic; font-size: 11.5px;
    color: var(--tagline); padding-left: 2px;
  }

  .motif {
    position: absolute; border-radius: 50%; background: var(--motif);
  }
  .card .motif--small { width: 120px; height: 120px; right: 18px; top: 146px; opacity: 0.55; }
  .motif--large { width: 210px; height: 215px; left: 170px; top: 42px; }

  .contact { position: absolute; left: 22px; top: 252px; font-size: 12.5px; color: var(--ink); line-height: 20px; }
  .contact b { font-weight: 700; }

  .person { position: absolute; left: 352px; top: 249px; color: var(--brown-dark); }
  .person__name { font-weight: 700; font-size: 15px; line-height: 20px; }
  .person__role { font-size: 14px; line-height: 20px; color: var(--ink); }

  .web {
    position: absolute; left: 22px; bottom: 7px; font-weight: 700; font-size: 15px; color: var(--white);
  }
  .web--back {
    left: 0; width: 100%; text-align: center; bottom: 34px;
    font-size: 13.5px; color: var(--brown-dark);
  }
</style>
</head>
<body>

  <section class="card card--front-1">
    <svg class="band band--top" viewBox="0 0 552 26" preserveAspectRatio="none">
      <polygon points="0,0 390,0 372,26 0,26" fill="var(--brown)"/>
      <polygon points="398,0 552,0 552,26 380,26" fill="var(--orange)"/>
    </svg>
    <div class="brand">
      <div class="brand__name"><span class="brand__dot"></span>Dribblecake Bites</div>
      <div class="brand__tagline">The Yummy Mini Dutch Pancakes</div>
    </div>
    <div class="motif motif--small" role="img" aria-label="Faint pancake character decoration"></div>
    <div class="contact">
      <div><b>P:</b> 0419362857</div>
      <div><b>E:</b> Percy.Lantern@dribblecakebites.com.au</div>
    </div>
    <div class="person">
      <div class="person__name">Percy Lantern</div>
      <div class="person__role">Managing Director</div>
    </div>
    <svg class="band band--bottom" viewBox="0 0 552 30" preserveAspectRatio="none">
      <polygon points="0,0 390,0 408,30 0,30" fill="var(--brown)"/>
      <polygon points="396,0 552,0 552,30 414,30" fill="var(--orange)"/>
    </svg>
    <div class="web">www.dribblecakebites.com.au</div>
  </section>

  <section class="card card--back-1">
    <div class="motif motif--large" role="img" aria-label="Large faint pancake character illustration"></div>
    <div class="web web--back">www.dribblecakebites.com.au</div>
  </section>

  <section class="card card--front-2">
    <svg class="band band--top" viewBox="0 0 552 26" preserveAspectRatio="none">
      <polygon points="0,0 390,0 372,26 0,26" fill="var(--brown)"/>
      <polygon points="398,0 552,0 552,26 380,26" fill="var(--orange)"/>
    </svg>
    <div class="brand">
      <div class="brand__name"><span class="brand__dot"></span>Dribblecake Bites</div>
      <div class="brand__tagline">The Yummy Mini Dutch Pancakes</div>
    </div>
    <div class="motif motif--small" role="img" aria-label="Faint pancake character decoration"></div>
    <div class="contact">
      <div><b>P:</b> 0417583926</div>
      <div><b>E:</b> Teodorblum@quillnet.com</div>
    </div>
    <div class="person">
      <div class="person__name">Teodor Blum</div>
      <div class="person__role">Business Manager</div>
    </div>
    <svg class="band band--bottom" viewBox="0 0 552 30" preserveAspectRatio="none">
      <polygon points="0,0 390,0 408,30 0,30" fill="var(--brown)"/>
      <polygon points="396,0 552,0 552,30 414,30" fill="var(--orange)"/>
    </svg>
    <div class="web">www.dribblecakebites.com.au</div>
  </section>

  <section class="card card--back-2">
    <div class="motif motif--large" role="img" aria-label="Large faint pancake character illustration"></div>
    <div class="web web--back">www.dribblecakebites.com.au</div>
  </section>

</body>
</html>
```